Banner Ad Design Project

hi i need several banner for a casino website
for examples you can visit some of the online casinos on the net.

the banners i need:

1. sportsbook
2. live casino
3. blackjack
4. slot games
5. bonus (e.g. Christmass bonus "double your deposit!" or "free spins"
6. "Do you want to win a trip to Las Vegas? Join now!"

if possible with some movement (flash/html5)

i have updated the prices!

payment committed! 

Reason: Error by brieflane End day was similar on start day

Industry/Entity Type

Casino

```html
<!DOCTYPE html>
<html lang="en">
<head>
<meta charset="UTF-8">
<title>Christmas Bonus Banner</title>
<link rel="stylesheet" href="https://fonts.googleapis.com/css2?family=Montserrat:wght@300;400&family=PT+Sans+Narrow:wght@700&family=Rubik:wght@800&display=swap">
<style>
  :root {
    --stage: #252525;
    --felt: #1f5a38;
    --felt-dark: #17472c;
    --gold: #e9b274;
    --white: #ffffff;
    --cta-red: #c8102e;
    --cta-border: #e8d9d9;
    --band-red: #b5122b;
    --paper: #ffffff;
    --paper-shade: #c9cfcc;
    --casino-green: #1db64a;
    --hat-red: #8f1421;
    --chip-tone: #b83a3a;
  }
  * { margin: 0; padding: 0; box-sizing: border-box; }
  html, body {
    width: 1200px; height: 900px; overflow: hidden;
    background: var(--stage);
  }
  .banner {
    position: absolute;
    left: 375px; top: 262px;
    width: 450px; height: 375px;
    overflow: hidden;
    background: linear-gradient(160deg, var(--felt) 0%, var(--felt-dark) 100%);
  }
  .banner__art {
    position: absolute; left: 0; top: 0;
    width: 450px; height: 375px;
  }
  .banner__eyebrow {
    position: absolute; left: 21px; top: 20px;
    font-family: "Montserrat", sans-serif; font-weight: 400;
    font-size: 22px; letter-spacing: 1.2px;
    color: var(--gold);
  }
  .banner__headline {
    position: absolute; left: 20px; top: 50px;
    font-family: "Montserrat", sans-serif; font-weight: 300;
    font-size: 40px; line-height: 49px;
    color: var(--white);
  }
  .banner__cta {
    position: absolute; left: 23px; top: 175px;
    width: 162px; height: 51px;
    display: flex; align-items: center; justify-content: center;
    background: var(--cta-red);
    border: 2px solid var(--cta-border);
    border-radius: 3px;
    font-family: "PT Sans Narrow", sans-serif; font-weight: 700;
    font-size: 23px; color: var(--white);
    text-decoration: none;
  }
  .banner__brand {
    position: absolute; left: 18px; top: 290px;
    font-family: "Rubik", sans-serif; font-weight: 800;
    font-size: 66px; letter-spacing: 2px; line-height: 1;
    color: var(--casino-green);
  }
</style>
</head>
<body>
  <div class="banner">
    <svg class="banner__art" viewBox="0 0 450 375" xmlns="http://www.w3.org/2000/svg">
      <defs>
        <linearGradient id="heroTones" x1="0" y1="0" x2="0" y2="1">
          <stop offset="0" stop-color="var(--hat-red)"/>
          <stop offset="0.45" stop-color="#d9d2c4"/>
          <stop offset="1" stop-color="var(--chip-tone)"/>
        </linearGradient>
        <linearGradient id="paperShade" x1="0" y1="0" x2="1" y2="0">
          <stop offset="0.55" stop-color="var(--paper)"/>
          <stop offset="1" stop-color="var(--paper-shade)"/>
        </linearGradient>
      </defs>
      <rect class="hero-photo" role="img" aria-label="Santa hat resting on a pile of red and blue casino chips" x="200" y="0" width="250" height="310" rx="30" fill="url(#heroTones)" opacity="0.9"/>
      <path class="divider-band" d="M0,238 Q160,278 450,290 L450,375 L0,375 Z" fill="var(--band-red)"/>
      <path class="lower-panel" d="M0,248 Q160,288 450,300 L450,375 L0,375 Z" fill="url(#paperShade)"/>
    </svg>
    <div class="banner__eyebrow">CHRISTMAS BONUS</div>
    <div class="banner__headline">Double your<br>Deposit!</div>
    <a class="banner__cta" href="#">JOIN TODAY</a>
    <div class="banner__brand">CASINO</div>
  </div>
</body>
</html>
```